Audio Visual Events Professional- Needs slick BC

I need a personal business card to network my freelance services as a live audio operator/AV technician around Australia.
Slick, professional, not overly colourful

Preferred tastes include sacred geometry, psychedelic, Celtic
Updates

Target Market(s)

Clients event industry- male and female 30-50

Industry/Entity Type

Business

Requirements
Must have
• details

Corwen Malloway

soundrig@techmailbox.net
0493 518 207
Nice to have
• Example of background, see image (Veltrix MX8)
Pattern covering unfocused area

Audio Visual Events Professional
Live Audio services
System Engineering

back side full pattern

```html
<!DOCTYPE html>
<html lang="en">
<head>
<meta charset="utf-8">
<title>Corwen Malloway – Business Card</title>
<link rel="stylesheet" href="https://fonts.googleapis.com/css2?family=Bebas+Neue&family=Oswald:wght@400;500&family=Ubuntu:wght@700&display=swap">
<style>
  :root {
    --page: #ffffff;
    --card-light: #7cc0e8;
    --card-mid: #4f9fd4;
    --card-deep: #2d74b5;
    --card-edge: #2b3a86;
    --panel: rgba(255, 255, 255, 0.72);
    --band: rgba(225, 236, 250, 0.85);
    --purple: #5b2a8c;
    --purple-deep: #3f1a6e;
    --navy: #1f2766;
  }
  * { margin: 0; padding: 0; box-sizing: border-box; }
  html, body { width: 1200px; height: 848px; overflow: hidden; background: var(--page); }
  .canvas { position: relative; width: 1200px; height: 848px; }

  .card {
    position: absolute; left: 330px; width: 542px; height: 340px;
    border-radius: 20px; border: 1.5px solid var(--card-edge);
    overflow: hidden;
  }
  .card--front { top: 57px; }
  .card--back  { top: 446px; }

  .card__frame {
    position: absolute; inset: 12px; border-radius: 14px;
    border: 1px solid rgba(255,255,255,0.35);
    pointer-events: none;
  }

  .console-photo {
    position: absolute; inset: 0;
    background: linear-gradient(160deg, var(--card-light) 0%, var(--card-mid) 45%, var(--card-deep) 100%);
  }

  .info-panel {
    position: absolute; left: 163px; top: 21px; width: 217px; height: 290px;
    background: var(--panel); border-radius: 8px;
  }

  .emblem {
    position: absolute; left: 231px; top: 27px; width: 80px; height: 80px;
    border-radius: 50%;
    background: radial-gradient(circle, #d9d2ee 0%, #9a7cc4 45%, var(--purple) 75%, var(--purple-deep) 100%);
  }

  .name-band {
    position: absolute; left: 0; right: 0; top: 135px; height: 50px;
    background: var(--band);
    border-top: 4px solid var(--purple);
    border-bottom: 4px solid var(--purple);
  }

  .details {
    position: absolute; left: 163px; width: 217px; top: 0; height: 340px;
    text-align: center; color: var(--navy);
  }
  .details__name {
    position: absolute; left: 0; right: 0; top: 146px;
    font-family: "Bebas Neue", sans-serif; font-size: 34px; font-weight: 400;
    letter-spacing: 0.5px; line-height: 1; white-space: nowrap;
  }
  .details__email {
    position: absolute; left: 0; right: 0; top: 197px;
    font-family: "Ubuntu", sans-serif; font-weight: 700; font-size: 15px;
    line-height: 18px; white-space: nowrap;
  }
  .details__phone {
    position: absolute; left: 0; right: 0; top: 217px;
    font-family: "Oswald", sans-serif; font-size: 16px; font-weight: 400;
    line-height: 20px;
  }
  .details__rule {
    position: absolute; left: 62px; width: 93px; top: 246px;
    height: 2px; background: var(--navy);
  }
  .details__services {
    position: absolute; left: 0; right: 0; top: 253px;
    list-style: none;
    font-family: "Oswald", sans-serif; font-size: 10px; line-height: 15.5px;
    text-transform: uppercase; letter-spacing: 0.2px; white-space: nowrap;
  }

  .back-pattern {
    position: absolute; inset: 0;
    background: radial-gradient(circle at 50% 50%, #8fd3ef 0%, #5fb3e0 55%, #3d86c6 100%);
  }
  .back-emblem {
    position: absolute; left: 124px; top: 22px; width: 294px; height: 294px;
    border-radius: 50%;
    background: radial-gradient(circle, #9fdcf2 0%, #7ec6ea 38%, #8c6fc0 62%, var(--purple) 82%, var(--purple-deep) 100%);
  }
</style>
</head>
<body>
<main class="canvas">

  <section class="card card--front" aria-label="Business card front">
    <div class="console-photo" role="img" aria-label="Photo of a Veltrix MX8 digital mixing console, soft blue tint"></div>
    <div class="card__frame"></div>
    <div class="info-panel"></div>
    <div class="name-band"></div>
    <div class="emblem" role="img" aria-label="Sacred geometry star emblem"></div>
    <div class="details">
      <h1 class="details__name">Corwen Malloway</h1>
      <p class="details__email">soundrig@techmailbox.net</p>
      <p class="details__phone">0493 518 207</p>
      <div class="details__rule"></div>
      <ul class="details__services">
        <li>Audio Visual Events Professional</li>
        <li>Live Audio Services</li>
        <li>System Engineering</li>
      </ul>
    </div>
  </section>

  <section class="card card--back" aria-label="Business card back">
    <div class="back-pattern" role="img" aria-label="Repeating interlocking circle pattern in light blue"></div>
    <div class="card__frame"></div>
    <div class="back-emblem" role="img" aria-label="Large sacred geometry star emblem"></div>
  </section>

</main>
</body>
</html>
```